Flyer for a Unique Type of Tax Services

Please refer to the attached sample design for reference. Feel free to change the wording as needed. Here is the project brief:

Objective:
Objective of this flyer is to introduce our services which we are launching soon, which is new of a kind, to our potential customers i.e. online tax return preparation. By looking at the flyer we want our target audience to get convinced of our services and visit our website and register with us. They don’t have to pay anything to register.

Our Competitors:
Currently there are three main options available to get tax returns prepared. First is to buy tax software and get tax return prepared at own, this is the cheapest option. There are studies that suggest that people who are not well aware of tax laws there are chances they miss certain tax refunds by filing returns at their own and potentially lose money. Second option is to go to the local offices of nation-wide tax service companies like Pell & Varne and Morrow Tandy. They open offices only during tax season i.e. Jan through April but they are not available other part of the year and their association with the customers is temporary. Third option is to go to a CPA office which are the most expensive and very few people go for this option.

Weaknesses of the Current Options:
By self-preparing tax returns, there are chances that one can overlook certain tax laws that can provide additional tax credits and exemptions to people and overall they could have got a higher tax refund from the Govt. but they may miss it.
By going to other competitors during the peak time when tax returns are due, there are high chances that they don't have enough time to do research to ensure maximum refunds based on the exact circumstances of the individuals at the peak time as many people come to them during that time. Also they are not available after the tax season to provide them any answers to their questions or provide them tax planning tips to help them save tax in the next season.
By going to the CPA office, they charge a lot of fees and also for any tax advice later during the year, they will charge additional fees.

What we are offering:
We are offering a new option i.e. online tax return preparation through experts. We'll charge the fees competitive to what people are paying to local tax providers. But we will be different than our competitors as we'll be providing value added service if they got their returns prepared through us. Value added services we will be free of any additional cost for our customers who'll get tax return prepared through us.

Our Target Audience:
Our target audience is any person or couple who go to the tax service providers like Pell & Varne or Morrow Tandy to get their tax returns prepared.

How We are Different:
Here is the summary of the unique aspects of our business as compared to the competitors:
- Customers just pay us the price for preparing the annual return and price is comparable and competitive to what they have been paying to other providers.
- Unlike our competitors, we do extensive research to review the circumstances of our customers and explore applicable tax laws to make sure all available tax credits, exemptions, and deductions are taken for our customers, whereas our customers don't usually do such kind of research as during the peak tax season when customers approach them they usually don’t have time to do that kind of research. We start our association with our customers much sooner than the actual due date and this provides us time to do extensive research and we try our best that our customers could get higher tax returns.
- By just getting tax returns prepared through us, we enter into a long-term association with our customers and provide them complimentary tax planning tips throughout the year to help them save tax in the following year
- We are available to our customers year-round to provide complementary answers to any tax related questions without any additional cost e.g. how to save tax when buying a car, whether to buy or lease the care to save tax, for the sole-proprietor business how to save tax by using portion of the home as home-office, how to save tax by using personal car for personal business.
- We also provide answers to other basic financial advise related matters e.g. which insurance product is better, whether full insurance or term-life insurance to chose, how to save for the retirement etc.

Other Details:
Our logo has already been designed and we want the same logo to be used in the flyer. Our website address is: www.FiledRightPlus.com (it is still under construction but to get perspective of what we are trying to offer, visit this alternate website that it not final yet but will give an idea: http://www.filedrightplus.com/wordpress. Fyi, a video at this link is only a placeholder and not relevant to our services)

Requirements
Must have
• Please refer to the sample flyer attached. Feel free to change the design and language.
Should not have
• Please do not put any testimonial on the flyer as reflected in the under construction website.

```html
<!DOCTYPE html>
<html lang="en">
<head>
<meta charset="utf-8">
<title>FiledRight Plus – Tax Services Flyer</title>
<link href="https://fonts.googleapis.com/css2?family=Open+Sans:ital,wght@0,400;0,600;0,700;0,800;1,600;1,700&display=swap" rel="stylesheet">
<style>
  :root {
    --navy: #1c2b4d;
    --orange: #f07a1a;
    --blue: #1f63c6;
    --text: #2b2b2b;
    --band: #4a4a4a;
    --paper: #ffffff;
  }
  * { box-sizing: border-box; margin: 0; padding: 0; }
  html, body { width: 745px; height: 1200px; overflow: hidden; background: var(--paper); }
  .flyer {
    position: relative; width: 745px; height: 1200px; overflow: hidden;
    font-family: "Open Sans", Arial, sans-serif; color: var(--text); background: var(--paper);
  }
  .hero { position: absolute; left: 0; top: 0; width: 745px; height: 510px; }
  .hero-photo {
    position: absolute; inset: 0;
    background: linear-gradient(160deg, #d9dde3 0%, #b9c1cc 45%, #8d98a8 75%, #c8ced6 100%);
  }
  .hero-shapes { position: absolute; left: 0; top: 0; }
  .headline {
    position: absolute; left: 0; top: 528px; width: 745px; text-align: center;
    color: var(--navy); font-weight: 800; font-size: 38px; line-height: 44px;
  }
  .content {
    position: absolute; left: 40px; top: 712px; width: 665px;
    display: flex; flex-direction: column;
  }
  .benefits { list-style: none; }
  .benefits li {
    position: relative; padding-left: 24px; font-size: 18px; line-height: 25px;
    color: var(--text); margin-bottom: 16px;
  }
  .benefits li::before {
    content: ""; position: absolute; left: 0; top: 8px; width: 10px; height: 10px; background: var(--orange);
  }
  .benefits strong { color: var(--navy); font-weight: 700; }
  .offer {
    margin-top: 8px; text-align: center; font-size: 18px; line-height: 26px; color: var(--navy);
  }
  .offer .lead { color: var(--orange); font-style: italic; font-weight: 700; }
  .register {
    margin-top: 26px; text-align: center;
    color: var(--orange); font-style: italic; font-weight: 700; font-size: 20px;
  }
  .register .url { color: var(--blue); }
  .brand {
    position: absolute; left: 0; top: 1046px; width: 745px; display: flex; justify-content: center; align-items: center; gap: 10px;
  }
  .brand-mark { width: 22px; height: 22px; background: var(--orange); }
  .brand-name { font-weight: 800; font-size: 30px; color: var(--blue); letter-spacing: 1px; }
  .footer-band {
    position: absolute; left: 0; top: 1108px; width: 745px; height: 92px; background: var(--band);
    color: #fff; font-size: 16px; line-height: 23px; text-align: left; padding: 10px 30px 0;
  }
</style>
</head>
<body>
<main class="flyer">
  <section class="hero">
    <div class="hero-photo" role="img" aria-label="Photo of a stressed man in a shirt and tie holding his head, surrounded by tax forms"></div>
    <svg class="hero-shapes" width="745" height="510" viewBox="0 0 745 510" aria-hidden="true">
      <polygon points="0,490 745,415 745,510 0,510" fill="#ffffff"/>
      <polygon points="420,465 745,345 745,380 440,475" fill="var(--orange)"/>
      <polygon points="470,468 745,395 745,430 490,468" fill="var(--blue)"/>
      <polygon points="0,488 745,413 745,428 0,503" fill="#e9ecf0"/>
    </svg>
  </section>

  <h1 class="headline">Does your Tax Return Preparer<br>has time to do extensive research<br>for you to get MAXIMUM REFUNDS?</h1>

  <div class="content">
    <ul class="benefits">
      <li>Do you get <strong>Year-Round Free Advice</strong> regrding your Tax Related Questions from your existing Tax Service Provider?</li>
      <li>Does your existing <strong>Tax Service Provider</strong> give you <strong>Complementary Tax Planning Tips</strong> throughout the year to help you save tax in the following financial year?</li>
    </ul>

    <p class="offer"><span class="lead">If not</span>, then try us as we do provide all these services year-round to our customers who get tax returns prepared through us at no additionaL COST.</p>

    <p class="register">Register now free at: <span class="url">www.FiledRightPlus.com</span></p>
  </div>

  <div class="brand">
    <span class="brand-mark"></span>
    <span class="brand-name">FILEDRIGHT PLUS</span>
  </div>

  <footer class="footer-band">And right away we'll start doing research for you and will be available year-round to answer you tax related queries and we will keep providing you tax planning tips and also provide you guideline on other financial planning matters.</footer>
</main>
</body>
</html>
```